Beautiful Simple and Clean WEbsite for Life Coach

Looking for a simple clean site website for life coach for educators. A home page will have an embedded opt-in form, menu bar will be
Work With Me - page for my coaching program and link to online calendar for booking
PRAISE - testimonials
ABOUT
PODCAST
I can supply images and a site I would like it modeled after is https://petrawendt.com/
My current website at www.dorabeckett.com is too dark. I am looking for the white space, pink and magenta. Feel free to use images from the site

Industry/Entity Type

Life Coaching

Number of Pages Required

4 page

Font styles to use
Serif

Colors
E54698
E96AAD
F1A4CE
F9D9EA
FCEFF6

Requirements
Must have
• See attached files for must-haves, Lots of white space, opt-in from for freebie is the most prominent on home page
Nice to have
• refer to Petra Wendt websites
Should not have
• dark colors, any balck background

```html
<!DOCTYPE html>
<html lang="en">
<head>
<meta charset="utf-8">
<title>Dora Beckett – Life Coach for Educators</title>
<link rel="stylesheet" href="https://fonts.googleapis.com/css2?family=Gelasio:wght@400;500&family=Poppins:wght@400;500&display=swap">
<style>
:root{
  --magenta:#E54698;
  --pink:#E96AAD;
  --rose:#F1A4CE;
  --blush:#F9D9EA;
  --mist:#FCEFF6;
  --ink:#1f1a1c;
  --text:#6b6468;
  --white:#ffffff;
}
*{margin:0;padding:0;box-sizing:border-box}
html,body{width:1200px;height:4717px;overflow:hidden;background:var(--white)}
body{position:relative;font-family:"Poppins",sans-serif;color:var(--text)}
.serif{font-family:"Gelasio",serif;color:var(--ink);font-weight:400}
section,header,footer{position:absolute;left:0;width:1200px}
.abs{position:absolute}
.center{text-align:center}
.para{font-size:13px;line-height:27px;color:var(--text)}
.btn{position:absolute;display:flex;align-items:center;justify-content:center;gap:10px;font-size:13px;font-weight:500}
.btn-solid{background:var(--magenta);color:var(--white)}
.btn-outline{border:2px solid var(--magenta);color:var(--magenta);background:var(--white)}
.photo{position:absolute}

/* header + hero */
.hero{top:0;height:640px;background:linear-gradient(120deg,var(--blush) 0%,var(--mist) 55%,#fde9f3 100%)}
.logo{font-family:"Gelasio",serif;color:var(--magenta);font-size:30px}
.nav{position:absolute;top:58px;left:455px;display:flex;gap:30px;font-family:"Gelasio",serif;font-size:13px;color:var(--ink)}
.hero h1{position:absolute;left:100px;top:180px;width:600px;font-size:49px;line-height:60px}

/* steps */
.steps{top:640px;height:408px}
.steps h2{position:absolute;top:710px;width:100%;font-size:50px}

/* about */
.about{top:1048px;height:696px;background:linear-gradient(160deg,var(--mist) 0%,var(--white) 40%,var(--blush) 100%)}

/* beginning */
.card-icon{position:absolute;width:176px;height:174px;background:var(--blush)}
.card-shadow{position:absolute;width:176px;height:174px;background:var(--mist)}
.card h3{position:absolute;width:300px;text-align:center;font-size:26px}
.card p{position:absolute;width:240px;text-align:center}

/* imagine */
.imagine{top:2506px;height:667px;background:var(--mist)}

/* testimonials */
.dot{position:absolute;width:9px;height:9px;border-radius:50%;background:var(--blush)}

/* book */
.book{top:3697px;height:443px;background:linear-gradient(180deg,var(--blush) 0%,var(--mist) 60%,var(--blush) 100%)}

.input{position:absolute;border:1px solid #ddd;background:var(--white);font-size:12px;color:#888;padding-left:16px;display:flex;align-items:center}
.foot-nav{position:absolute;top:4618px;width:100%;display:flex;justify-content:center;gap:30px;font-size:12px;color:var(--text)}
.small{font-size:12px;color:var(--text)}
.tiny{font-size:9px;color:var(--text)}
</style>
</head>
<body>

<!-- Header and hero -->
<section class="hero">
  <div class="abs logo" style="left:100px;top:46px">Dora Beckett</div>
  <nav class="nav"><span>WORK WITH ME</span><span>PRAISE</span><span>ABOUT ME</span><span>PODCASTS</span></nav>
  <div class="btn btn-solid" style="left:987px;top:46px;width:112px;height:42px">Book Now</div>

  <h1 class="serif">Amet minim mollit non aliqua dolor amet sint.</h1>
  <p class="abs para" style="left:100px;top:334px;width:470px">Amet minim mollit non deserunt ullamco est sit aliqua dolor do amet sint. Velit officia consequat duis enim velit mollit. Exercitation veniam consequat sunt nostrud amet.</p>
  <div class="btn btn-solid" style="left:100px;top:458px;width:140px;height:40px">Learn more
    <svg width="12" height="12" viewBox="0 0 12 12"><path d="M1 6h9M6 2l4 4-4 4" stroke="#fff" stroke-width="1.6" fill="none"/></svg></div>
  <div class="photo" role="img" aria-label="Portrait of the coach in a wide straw hat and denim jacket" style="left:690px;top:146px;width:400px;height:494px;border-radius:200px 200px 0 0;background:linear-gradient(180deg,#d9c49a 0%,#d9c49a 22%,#f1d7c8 32%,#5d6e72 55%,#4a5a60 100%)"></div>
</section>

<!-- Free guide -->
<section class="steps">
  <h2 class="serif center" style="top:70px">The 5 Steps to make it Happen</h2>
  <p class="abs para center" style="left:210px;top:167px;width:780px">Amet minim mollit non deserunt ullamco est sit aliqua dolor do amet sint. Velit officia consequat duis enim velit mollit. Exercitation veniam consequat sunt nostrud amet. Amet minim mollit non deserunt ullamco est sit consequat sunt nostrud amet.</p>
  <div class="btn btn-outline" style="left:498px;top:289px;width:204px;height:43px">Download Free Guide
    <svg width="12" height="12" viewBox="0 0 12 12"><path d="M6 1v9M2 6l4 4 4-4" stroke="#E54698" stroke-width="1.6" fill="none"/></svg></div>
</section>

<!-- About -->
<section class="about">
  <div class="abs" role="img" aria-label="Faint dandelion seed head" style="left:740px;top:300px;width:330px;height:396px;background:radial-gradient(circle at 50% 35%,rgba(241,164,206,.55) 0%,rgba(249,217,234,.35) 40%,rgba(255,255,255,0) 70%)"></div>
  <div class="abs" style="left:150px;top:174px;width:409px;height:409px;background:var(--rose);opacity:.8"></div>
  <div class="photo" role="img" aria-label="Smiling portrait of the coach in a straw hat" style="left:100px;top:124px;width:409px;height:409px;background:linear-gradient(180deg,#7f8a5a 0%,#d8c08e 30%,#f0d0bf 55%,#f4f1ee 85%)"></div>
  <h2 class="abs serif" style="left:685px;top:124px;font-size:42px">Hi, I'm Dora Beckett!</h2>
  <p class="abs para" style="left:685px;top:218px;width:410px">Amet minim mollit non deserunt ullamco est sit aliqua dolor do amet sint. Velit officia consequat duis enim velit mollit. Exercitation veniam consequat sunt nostrud amet. Amet minim mollit non deserunt ullamco est sit aliqua dolor do amet sint. Velit officia consequat duis enim velit mollit. Exercitation veniam consequat sunt nostrud amet.</p>
  <div class="btn btn-solid" style="left:685px;top:428px;width:140px;height:43px">Learn more
    <svg width="12" height="12" viewBox="0 0 12 12"><path d="M1 6h9M6 2l4 4-4 4" stroke="#fff" stroke-width="1.6" fill="none"/></svg></div>
</section>

<!-- Start here -->
<section class="beginning" style="top:1744px;height:762px">
  <h2 class="serif center abs" style="top:84px;width:100%;font-size:50px">Let's start at the Beginning</h2>

  <div class="card">
    <div class="card-shadow" style="left:152px;top:238px"></div>
    <div class="card-icon" style="left:132px;top:218px"></div>
    <svg class="abs" style="left:180px;top:264px" width="80" height="80" viewBox="0 0 80 80" fill="none" stroke="#E54698" stroke-width="3"><path d="M8 18h46v34H34l-10 10V52H8z"/><path d="M18 30h24M18 40h20"/><path d="M50 36l16-22 6 5-16 22-8 2z"/></svg>
    <h3 class="serif" style="left:79px;top:450px">Read the Blog</h3>
    <p class="para" style="left:109px;top:500px">Amet minim mollit non deserunt ullamco est sit aliqua dolor do amet sint. Exercitation veniam consequat sunt nostrud amet.</p>
    <div class="btn btn-outline" style="left:167px;top:625px;width:125px;height:44px;font-size:12px">Read the Blog</div>
  </div>

  <div class="card">
    <div class="card-shadow" style="left:522px;top:238px"></div>
    <div class="card-icon" style="left:502px;top:218px"></div>
    <svg class="abs" style="left:550px;top:264px" width="80" height="80" viewBox="0 0 80 80" fill="none" stroke="#E54698" stroke-width="3"><circle cx="40" cy="36" r="30"/><circle cx="40" cy="36" r="18"/><circle cx="40" cy="32" r="6" fill="#E54698"/><rect x="35" y="40" width="10" height="26" rx="5" fill="#E54698"/></svg>
    <h3 class="serif" style="left:449px;top:450px">Listen to Podcast</h3>
    <p class="para" style="left:479px;top:500px">Amet minim mollit non deserunt ullamco est sit aliqua dolor do amet sint. Exercitation veniam consequat sunt nostrud amet.</p>
    <div class="btn btn-outline" style="left:537px;top:625px;width:125px;height:44px;font-size:12px">Listen Podcast</div>
  </div>

  <div class="card">
    <div class="card-shadow" style="left:892px;top:238px"></div>
    <div class="card-icon" style="left:872px;top:218px"></div>
    <svg class="abs" style="left:920px;top:264px" width="80" height="80" viewBox="0 0 80 80" fill="none" stroke="#E54698" stroke-width="3"><path d="M6 10h46v30H22l-10 10V40H6z"/><path d="M16 22h26M16 30h18"/><path d="M58 24h16v34h-6v10L58 58H30V46"/></svg>
    <h3 class="serif" style="left:819px;top:450px">Chat with us</h3>
    <p class="para" style="left:849px;top:500px">Amet minim mollit non deserunt ullamco est sit aliqua dolor do amet sint. Exercitation veniam consequat sunt nostrud amet.</p>
    <div class="btn btn-outline" style="left:907px;top:625px;width:125px;height:44px;font-size:12px">Chat with us</div>
  </div>
</section>

<!-- Imagine -->
<section class="imagine">
  <div class="abs" style="left:100px;top:130px;width:501px;height:407px;background:var(--white)"></div>
  <h2 class="abs serif" style="left:155px;top:196px;font-size:42px">Imagine a Life with</h2>
  <p class="abs para" style="left:155px;top:282px;width:390px">Amet minim mollit non deserunt ullamco est sit aliqua dolor do amet sint. Velit officia consequat duis enim velit mollit. Exercitation veniam consequat sunt nostrud amet. Amet minim mollit non deserunt ullamco est sit aliqua dolor do amet sint. Velit officia consequat duis enim velit mollit. Exercitation veniam consequat sunt nostrud amet.</p>
  <div class="photo" role="img" aria-label="Woman with arms open facing the sea at sunset" style="left:601px;top:130px;width:498px;height:407px;background:linear-gradient(160deg,#fbeee2 0%,#f4c8a8 35%,#d9b8b4 60%,#9a6e5e 100%)"></div>
</section>

<!-- Testimonials -->
<section class="testimonials" style="top:3173px;height:524px">
  <h2 class="serif center abs" style="top:80px;width:100%;font-size:50px">What they say?</h2>
  <svg class="abs" style="left:96px;top:273px" width="22" height="40" viewBox="0 0 22 40"><path d="M18 2L4 20l14 18" stroke="#bbb" stroke-width="2" fill="none"/></svg>
  <svg class="abs" style="left:1082px;top:273px" width="22" height="40" viewBox="0 0 22 40"><path d="M4 2l14 18L4 38" stroke="#bbb" stroke-width="2" fill="none"/></svg>
  <div class="photo" role="img" aria-label="Portrait of a client wearing a headscarf" style="left:169px;top:209px;width:168px;height:168px;border-radius:50%;background:linear-gradient(180deg,#c9b7a6 0%,#d9c5b2 45%,#8a7462 100%)"></div>
  <div class="abs" style="left:282px;top:202px;width:28px;height:28px;border-radius:50%;background:var(--blush);color:var(--magenta);font-family:'Gelasio',serif;font-size:22px;line-height:34px;text-align:center">”</div>
  <p class="abs para" style="left:420px;top:198px;width:610px">Amet minim mollit non deserunt ullamco est sit aliqua dolor do amet sint. Velit officia consequat duis enim velit mollit. Exercitation veniam consequat sunt nostrud amet.Amet minim mollit non deserunt ullamco est sit aliqua dolor do amet sint. Velit officia consequat duis enim velit mollit. Exercitation veniam consequat sunt nostrud amet.</p>
  <div class="abs serif" style="left:420px;top:328px;font-size:24px">Joan Pellis</div>
  <div class="abs small" style="left:420px;top:366px">Harlow Co.</div>
  <div class="dot" style="left:571px;top:440px"></div>
  <div class="dot" style="left:587px;top:440px;background:var(--magenta)"></div>
  <div class="dot" style="left:603px;top:440px"></div>
  <div class="dot" style="left:619px;top:440px"></div>
</section>

<!-- Book a call -->
<section class="book">
  <div class="abs" role="img" aria-label="Faint dandelion seed head" style="left:120px;top:190px;width:270px;height:253px;background:radial-gradient(circle at 50% 40%,rgba(190,130,160,.45) 0%,rgba(241,164,206,.3) 35%,rgba(255,255,255,0) 70%)"></div>
  <h2 class="serif center abs" style="top:100px;width:100%;font-size:50px">Book a Mindset Reset Call</h2>
  <p class="abs para center" style="left:270px;top:190px;width:660px">Amet minim mollit non deserunt ullamco est sit aliqua dolor do amet sint. Velit officia consequat duis enim velit mollit. Exercitation veniam consequat sunt nostrud amet.</p>
  <div class="btn btn-solid" style="left:535px;top:287px;width:130px;height:42px">Book Now
    <svg width="12" height="12" viewBox="0 0 12 12"><path d="M1 6h9M6 2l4 4-4 4" stroke="#fff" stroke-width="1.6" fill="none"/></svg></div>
</section>

<!-- Newsletter -->
<section class="newsletter" style="top:4140px;height:200px">
  <h2 class="serif abs" style="left:356px;top:78px;font-size:32px">Subscribe to our Newsletter</h2>
  <svg class="abs" style="left:270px;top:129px" width="42" height="40" viewBox="0 0 42 40" fill="none" stroke="#E54698" stroke-width="2"><path d="M3 16l18-13 18 13v21H3z"/><path d="M3 16l18 13 18-13"/><path d="M10 12h22v10"/></svg>
  <div class="input" style="left:353px;top:127px;width:420px;height:41px">Enter your email</div>
  <div class="btn btn-solid" style="left:815px;top:127px;width:115px;height:41px">Subscribe</div>
</section>

<!-- Footer -->
<footer style="top:4340px;height:377px">
  <div class="photo" role="img" aria-label="Round portrait of the coach in a straw hat" style="left:529px;top:29px;width:140px;height:140px;border-radius:50%;background:linear-gradient(180deg,#8d8a6a 0%,#cdb68a 35%,#efd2c2 60%,#f3efec 100%)"></div>
  <div class="abs logo center" style="top:196px;width:100%;font-size:28px">Dora Beckett</div>
  <svg class="abs" style="left:140px;top:264px" width="12" height="16" viewBox="0 0 12 16"><path d="M6 15s5-5.5 5-9A5 5 0 0 0 1 6c0 3.5 5 9 5 9z" fill="none" stroke="#E96AAD" stroke-width="1.5"/><circle cx="6" cy="6" r="1.8" fill="#E96AAD"/></svg>
  <div class="abs small" style="left:172px;top:250px;line-height:25px">2481 Maple Row, Ashford,<br>Vermont 05231</div>
  <nav class="foot-nav" style="top:278px"><span>Home</span><span>FAQs</span><span>About</span><span>Blog</span><span>Praise</span></nav>
  <svg class="abs" style="left:884px;top:243px" width="14" height="14" viewBox="0 0 14 14"><path d="M3 1l3 3-2 2a8 8 0 0 0 4 4l2-2 3 3-2 2C6 13 1 8 1 3z" fill="none" stroke="#E96AAD" stroke-width="1.3"/></svg>
  <div class="abs small" style="left:918px;top:241px">(555) 014-2290</div>
  <svg class="abs" style="left:884px;top:278px" width="14" height="14" viewBox="0 0 14 14"><circle cx="7" cy="7" r="6" fill="#F1A4CE"/></svg>
  <div class="abs small" style="left:915px;top:276px">info@dorabeckett.com</div>
  <div class="abs" style="left:100px;top:313px;width:1000px;height:1px;background:#eee"></div>
  <div class="abs tiny" style="left:143px;top:337px">Terms of Service &nbsp;|&nbsp; Privacy Policy</div>
  <div class="abs tiny center" style="top:337px;width:100%;font-size:10px">© Copyright 2022 by Dora Beckett</div>
  <div class="abs" style="left:948px;top:334px;width:18px;height:18px;border-radius:50%;background:var(--rose)"></div>
  <div class="abs" style="left:992px;top:334px;width:18px;height:18px;border-radius:50%;background:var(--rose)"></div>
  <div class="abs" style="left:1036px;top:334px;width:18px;height:18px;border-radius:50%;background:var(--rose)"></div>
</footer>

</body>
</html>
```